Corvellan Hotel

A Hotel (Pub) in Sydney CBD. Posters will be outside of Hotel informing People what is on in Hotel.
We will be Printing in A1 size.
CORVELLAN HOTEL
Open 9am - 3am 7 Days
Monday - Thursday
Happy Hour
4pm - 6pm
Local Beer & Wine
Wednesday
Poker Night: Great $$$ Prizes
Everyday
Steak or Schniztels: Served with Mashed Potato & Salad or Chips & Salad - $8.50
Live Sport on the Big Screen
BISTRO
OPEN 7 DAYS 12- 9pm
Daily Blackboard Specials + Full Menu Inside
Best service in Town
Male or Female 18 to Seniors.Passing Trade.
Hotel

```html
<!DOCTYPE html>
<html lang="en">
<head>
<meta charset="utf-8">
<title>Corvellan Hotel – What's On Poster</title>
<link rel="stylesheet" href="https://fonts.googleapis.com/css2?family=PT+Sans:wght@400;700&family=Kaushan+Script&display=swap">
<style>
  :root {
    --red: #e3141b;
    --red-dark: #b50d12;
    --ink: #1a1a1a;
    --white: #ffffff;
    --grey-light: #e9e9ea;
    --grey-mid: #b9b9bc;
    --grey-dark: #7d7d82;
    --cream: #fff3c4;
    --stage: #ececec;
  }
  * { box-sizing: border-box; margin: 0; padding: 0; }
  html, body {
    width: 1200px; height: 900px; overflow: hidden;
    background: var(--stage);
    font-family: "PT Sans", Arial, sans-serif;
  }
  .poster {
    position: absolute; left: 295px; top: 27px;
    width: 610px; height: 846px;
    background: var(--white);
    overflow: hidden;
    box-shadow: 0 4px 18px rgba(0,0,0,.18);
  }
  .poster-shapes { position: absolute; inset: 0; }
  .building-photo {
    position: absolute; left: 0; top: 330px; width: 610px; height: 440px;
    background:
      linear-gradient(180deg, rgba(255,255,255,1) 0%, rgba(255,255,255,.35) 30%, rgba(255,255,255,0) 55%),
      linear-gradient(90deg, #8f8f94 0%, #c9c8c6 35%, #a9a7a4 60%, #6f6e72 100%);
  }
  .header { position: absolute; left: 40px; top: 30px; color: var(--white); }
  .header-name { font-size: 29px; font-weight: 700; letter-spacing: .5px; }
  .header-hours { font-size: 27px; font-weight: 700; color: var(--cream); margin-top: 2px; }
  .brand-mark {
    position: absolute; right: 26px; top: 28px;
    display: flex; align-items: center; gap: 8px;
    font-size: 20px; font-weight: 700; color: var(--white);
  }
  .brand-mark .dot { width: 14px; height: 14px; border-radius: 50%; background: var(--white); }
  .everyday { position: absolute; left: 40px; top: 245px; color: var(--ink); }
  .everyday h2 { font-size: 38px; font-weight: 700; line-height: 1.1; }
  .everyday p { font-size: 22px; line-height: 1.2; }
  .live-sport { position: absolute; left: 40px; top: 395px; font-size: 22px; color: var(--ink); }
  .bistro { position: absolute; left: 40px; top: 452px; color: var(--ink); }
  .bistro h2 { font-size: 38px; font-weight: 700; line-height: 1.1; }
  .bistro p { font-size: 22px; line-height: 1.2; }
  .poker {
    position: absolute; left: 392px; top: 148px; width: 230px; height: 230px;
    border-radius: 50%; background: var(--white);
    border: 4px solid var(--grey-light);
    box-shadow: 0 2px 10px rgba(0,0,0,.15);
    text-align: center; color: var(--ink);
  }
  .poker-prizes { font-size: 20px; font-weight: 700; margin-top: 30px; margin-right: 20px; }
  .poker-chips {
    width: 110px; height: 80px; margin: 8px auto 0 40px; border-radius: 10px;
    background: linear-gradient(135deg, #c1272d 0%, #2e8b3a 50%, #1d1d1d 100%);
  }
  .poker-night { font-size: 20px; line-height: 1.05; margin-top: 6px; margin-left: 60px; text-align: left; }
  .fireworks {
    position: absolute; left: 275px; top: 612px; width: 232px; height: 180px;
    border-radius: 40% 40% 10% 10%;
    background: radial-gradient(circle at 50% 85%, #ffe14d 0%, #f49a1a 30%, #d6337a 55%, #3f7be0 75%, rgba(63,123,224,0) 90%);
  }
  .best-service {
    position: absolute; left: 339px; top: 756px; width: 156px; height: 68px;
    background: var(--white); border: 3px solid var(--red);
    text-align: center; font-weight: 700; line-height: 1.1; padding-top: 8px;
  }
  .best-service .line-1 { color: var(--red); font-size: 22px; }
  .best-service .line-2 { color: var(--ink); font-size: 22px; }
  .happy-hour { position: absolute; left: 10px; top: 706px; width: 200px; height: 134px; }
  .happy-hour-disc {
    position: absolute; left: 66px; top: 0; width: 134px; height: 134px;
    border-radius: 50%; background: var(--ink); border: 3px solid var(--white);
  }
  .happy-hour-label {
    position: absolute; left: 0; top: 24px; width: 172px; height: 36px;
    background: var(--white); border-radius: 18px;
    font-family: "Kaushan Script", cursive; color: var(--red);
    font-size: 25px; line-height: 36px; text-align: center;
  }
  .happy-hour-times {
    position: absolute; left: 66px; top: 68px; width: 134px;
    color: var(--white); text-align: center; line-height: 1.15;
  }
  .happy-hour-times .time { font-size: 20px; font-weight: 700; }
  .happy-hour-times .drinks { font-size: 12px; }
</style>
</head>
<body>
<main class="poster">
  <div class="building-photo" role="img" aria-label="Photograph of the hotel building facade on a city street corner"></div>

  <svg class="poster-shapes" width="610" height="846" viewBox="0 0 610 846" aria-hidden="true">
    <path d="M0 0 H610 V118 C470 150 300 185 0 168 Z" fill="var(--red)"/>
    <path d="M0 168 C300 185 470 150 610 118 V150 C470 190 300 215 0 200 Z" fill="var(--grey-light)"/>
    <path d="M0 200 C300 215 470 190 610 150 V162 C470 200 300 228 0 214 Z" fill="var(--grey-mid)" opacity=".6"/>
    <path d="M0 775 C180 740 420 760 610 705 V846 H0 Z" fill="var(--red)"/>
    <path d="M0 765 C180 730 420 748 610 693 V705 C420 760 180 740 0 775 Z" fill="var(--grey-light)"/>
  </svg>

  <header class="header">
    <h1 class="header-name">CORVELLAN HOTEL</h1>
    <p class="header-hours">Open 9am - 3am 7 Days</p>
  </header>

  <div class="brand-mark"><span class="dot"></span>Corvellan Hotel</div>

  <section class="everyday">
    <h2>Everyday</h2>
    <p>Steak or Schniztels:<br>Served with Mashed Potato<br>&amp; Salad or Chips &amp; Salad - $8.50</p>
  </section>

  <p class="live-sport">Live Sport on the Big Screen</p>

  <section class="bistro">
    <h2>BISTRO</h2>
    <p>OPEN 7 DAYS 12- 9pm<br>Daily Blackboard Specials + Full Menu Inside</p>
  </section>

  <section class="poker">
    <p class="poker-prizes">Great $$$ Prizes</p>
    <div class="poker-chips" role="img" aria-label="Stacks of red, green and black poker chips"></div>
    <p class="poker-night">Wednesday<br>Poker Night</p>
  </section>

  <div class="fireworks" role="img" aria-label="Colourful burst of celebration streamers and stars"></div>

  <div class="best-service">
    <div class="line-1">BEST SERVICE</div>
    <div class="line-2">IN TOWN</div>
  </div>

  <section class="happy-hour">
    <div class="happy-hour-disc"></div>
    <div class="happy-hour-label">Happy Hour</div>
    <div class="happy-hour-times">
      <div class="time">4pm - 6pm</div>
      <div class="drinks">Local Beer &amp; Wine</div>
    </div>
  </section>
</main>
</body>
</html>
```